Website for Tarrowby Oakleaf Club

Hi I require a website design in WordPress.

It is for a Diggers Club (KVA or Club, Hotel/Restaurant).

It will have a section for the club with blogs and news as well as announcements of upcoming events on the front page.

Another major component of the site will be the Chinese restaurant which will have information about the restaurant as well as the ability to order food online (using a eCommerce module at this stage).

I have included the logos for the shop, as well as some hand drawn images that the Chinese restaurant will want included into their page. This may require a vector to be created that is of the same image (must be EXACTLY the same as the images are highly symbolic).

I am happy to increase the budget to include this vector graphic creation upon request and successful submission.

It would be desired for this to be delivered as coded HTML/CSS or Wordpress, however this is negotiable.

Hi all, thanks for the great submissions,.

Just to clarify. This is a pub (hotel, or ex-services club) that has a restaurant. The restaurant is an important aspect the the site, but not the only focus.

Unfortunately the client has offered very little directly, however the front page will need to be a balance of the Resaurant, bar, and the community sentiment of being a ex-services club, I have added some extra images. These may not suiit the website, but show what an kva is.

Locals who are looking for a nice place to drink, or good quality food.

Restaurant

```html
<!DOCTYPE html>
<html lang="en">
<head>
<meta charset="utf-8">
<title>Tarrowby Oakleaf Club</title>
<link href="https://fonts.googleapis.com/css2?family=Noto+Serif:ital,wght@0,400;0,700;1,400&family=Open+Sans:wght@400;600;700&display=swap" rel="stylesheet">
<style>
:root{
  --page:#ebe8e3;
  --card:#f4f2ee;
  --line:#d9d5ce;
  --ink:#333;
  --muted:#777;
  --accent:#e8461e;
  --dark:#1b1b1b;
  --darker:#111;
  --footer:#151515;
  --footer-head:#d9c44d;
  --white:#fff;
}
*{box-sizing:border-box;margin:0;padding:0}
html,body{width:1200px;height:3333px;overflow:hidden}
body{background:var(--page);font-family:"Open Sans",Arial,sans-serif;color:var(--ink);font-size:13px;line-height:1.55}
a{color:inherit;text-decoration:none}

/* top bar */
.topbar{height:41px;background:var(--darker);color:#ccc;font-size:11px;display:flex;justify-content:flex-end;align-items:center;gap:22px;padding-right:197px}
.topbar span{display:flex;align-items:center;gap:6px}
.topbar svg{width:11px;height:11px;fill:#ccc}

/* header */
.site-header{height:100px;background:var(--dark);display:flex;align-items:center;justify-content:space-between;padding:0 187px 0 185px}
.brand{display:flex;align-items:center;gap:10px;font-family:"Noto Serif",Georgia,serif;font-size:22px;color:#e8c530;line-height:1.05;width:230px}
.brand-dot{width:22px;height:22px;border-radius:50%;background:var(--accent);flex:none}
.main-nav{display:flex;gap:30px}
.main-nav a{display:flex;flex-direction:column;align-items:center;gap:6px;font-family:"Noto Serif",Georgia,serif;font-weight:700;font-size:15px;color:#eee}
.main-nav a.active{color:var(--accent)}
.main-nav svg{width:14px;height:14px;fill:currentColor}

/* hero */
.hero{position:relative;height:569px;background:radial-gradient(ellipse at 45% 40%,#7a1a12 0%,#4a120d 45%,#241410 80%,#1a1412 100%)}
.hero-arrow{position:absolute;top:268px;width:34px;height:34px;display:flex;align-items:center;justify-content:center}
.hero-arrow svg{width:14px;height:14px;fill:none;stroke:#fff;stroke-width:3}
.hero-arrow.prev{left:12px}.hero-arrow.next{right:12px}
.hero-dots{position:absolute;bottom:18px;left:50%;transform:translateX(-50%);display:flex;gap:6px}
.hero-dots i{width:13px;height:13px;border-radius:50%;border:2px solid #fff;background:rgba(255,255,255,.35)}
.hero-dots i:first-child{background:#fff}

/* main */
.container{width:830px;margin:0 auto}
.section-title{font-family:"Noto Serif",Georgia,serif;font-style:italic;font-size:21px;color:#333;height:28px;line-height:28px}

.features{margin-top:54px;height:292px;display:grid;grid-template-columns:repeat(4,1fr);gap:20px}
.feature{background:var(--card);border:4px solid #e2ded7;text-align:center;padding:38px 22px 0}
.feature svg{width:66px;height:66px}
.feature h3{font-family:"Noto Serif",Georgia,serif;font-weight:400;color:var(--accent);font-size:16px;margin:30px 0 14px}
.feature p{font-size:11.5px;color:var(--muted);line-height:1.6}

.order-title{margin-top:36px}
.products{margin-top:8px;height:392px;display:grid;grid-template-columns:repeat(3,1fr);gap:14px}
.product{background:var(--white);display:flex;flex-direction:column}
.product .photo{height:270px}
.product .name{display:flex;justify-content:space-between;align-items:center;padding:0 10px;height:50px;border-bottom:2px solid var(--line);font-family:"Noto Serif",Georgia,serif;font-style:italic;font-size:13px}
.veg{width:15px;height:15px;border:2px solid var(--accent);display:flex;align-items:center;justify-content:center}
.veg::after{content:"";width:7px;height:7px;border-radius:50%;background:var(--accent)}
.product .buy{display:flex;justify-content:space-between;align-items:center;padding:0 10px;flex:1}
.btn{background:var(--accent);color:#fff;font-size:12px;padding:8px 14px;display:inline-block}
.price{font-weight:700;font-size:13px}
.p1{background:linear-gradient(160deg,#c9a56a,#8a5a2a 55%,#efe7d8)}
.p2{background:linear-gradient(160deg,#6a3a25,#3b1f18 55%,#7a2a3a)}
.p3{background:linear-gradient(160deg,#9a3a10,#5a200a 55%,#c06020)}

.events-title{margin-top:72px}
.events{height:308px;display:grid;grid-template-columns:1fr 1fr;gap:20px}
.event{display:flex}
.event-side{width:90px;flex:none}
.event-date{height:40px;display:flex;align-items:flex-start;gap:4px;font-family:"Noto Serif",Georgia,serif;font-style:italic}
.event-date b{font-weight:400;font-size:30px;line-height:1}
.event-date small{font-size:11px;line-height:1.15;padding-top:2px}
.event-stat{width:90px;height:52px;background:#555;color:#fff;display:flex;align-items:center;justify-content:center;font-size:12px;gap:6px;border-bottom:1px solid #777}
.event-stat.icon{background:#3a3a3a}
.event-stat svg{width:16px;height:16px;fill:#fff}
.event-card{flex:1;background:var(--white);display:flex;flex-direction:column}
.event-card .photo{height:130px}
.e1{background:linear-gradient(135deg,#3a3028,#8a7060 60%,#2a2420)}
.e2{background:linear-gradient(135deg,#7a1010,#c02828 55%,#3a0a0a)}
.event-card h4{font-family:"Noto Serif",Georgia,serif;font-style:italic;font-weight:400;font-size:16px;padding:26px 18px 12px;border-bottom:1px solid #eee}
.event-card p{font-size:11px;color:#666;padding:12px 18px;line-height:1.55;flex:1}
.event-meta{background:var(--darker);color:#ddd;font-size:10px;height:30px;display:flex;align-items:center;gap:12px;padding:0 12px}

.pager{margin-top:44px;height:30px;display:flex;align-items:center;gap:10px;font-size:11px;color:#555}
.pager a{width:26px;height:26px;display:flex;align-items:center;justify-content:center;background:#ddd}
.pager a.current{background:var(--accent);color:#fff}

.spec-title{margin-top:30px}
.tabs{height:48px;background:var(--darker);display:flex}
.tabs a{color:#fff;font-family:"Noto Serif",Georgia,serif;font-size:13px;display:flex;align-items:center;padding:0 16px;border-right:1px solid #444}
.tabs a.active{background:var(--accent)}
.tab-panel{height:174px;background:var(--card);padding:20px 26px}
.tab-panel h3{font-family:"Noto Serif",Georgia,serif;font-weight:400;font-size:21px;color:#444;padding-bottom:10px;border-bottom:1px solid var(--line);margin-bottom:10px}
.tab-panel p{font-size:11.5px;color:#777;line-height:1.6}

.upcoming-title{margin-top:50px}
.upcoming{height:280px;display:grid;grid-template-columns:repeat(3,1fr);gap:14px;margin-top:10px}
.upcoming .photo{height:136px}
.u1{background:linear-gradient(135deg,#2a1a12,#b07040 50%,#3a2010)}
.u2{background:linear-gradient(135deg,#3a1a0a,#c08030 50%,#2a1008)}
.u3{background:linear-gradient(135deg,#2a2220,#6a5040 50%,#a07050)}
.upcoming h4{font-family:"Noto Serif",Georgia,serif;font-weight:400;font-size:20px;margin-top:14px;color:#333}
.upcoming .when{font-size:10px;color:#888;display:flex;align-items:center;gap:5px;margin:2px 0 8px}
.upcoming .when svg{width:10px;height:10px;fill:#888}
.upcoming p{font-size:11.5px;color:#777;line-height:1.55}

.newsletter{margin-top:40px;height:128px;background:var(--white);border-left:6px solid var(--accent);padding:18px 32px}
.newsletter h3{font-family:"Noto Serif",Georgia,serif;font-style:italic;font-weight:400;font-size:21px}
.newsletter p{font-size:11px;color:#666;margin-bottom:14px}
.newsletter form{display:flex;gap:18px}
.newsletter input{width:290px;height:34px;border:none;background:#eee;padding:0 14px;font-family:inherit;font-size:11px;color:#999}
.newsletter button{background:var(--accent);color:#fff;border:none;height:34px;width:104px;font-family:inherit;font-size:13px}

/* footer */
.site-footer{margin-top:82px;height:400px;background:var(--footer);color:#ccc}
.footer-cols{width:830px;margin:0 auto;padding-top:40px;display:grid;grid-template-columns:200px 200px 210px 180px;gap:14px}
.footer-cols h5{font-family:"Noto Serif",Georgia,serif;font-style:italic;font-weight:400;color:var(--footer-head);font-size:17px;padding-bottom:4px;border-bottom:2px solid #444;margin-bottom:18px}
.post{display:flex;gap:8px;margin-bottom:16px;font-size:11px;line-height:1.45}
.post .thumb{width:52px;height:52px;flex:none;border:2px solid var(--footer-head);background:linear-gradient(135deg,#4a3a2a,#8a6a4a)}
.post b{color:var(--footer-head);font-family:"Noto Serif",Georgia,serif;font-style:italic;font-weight:400;display:block}
.gallery{display:grid;grid-template-columns:repeat(3,58px);gap:8px}
.gallery i{height:52px;border:2px solid var(--footer-head);background:linear-gradient(135deg,#5a2a1a,#b06a3a)}
.gallery i:nth-child(2n){background:linear-gradient(135deg,#2a2a3a,#8a6a50)}
.contact li{list-style:none;display:flex;gap:8px;font-size:11px;margin-bottom:12px}
.contact svg{width:11px;height:11px;fill:#ccc;flex:none;margin-top:3px}
.contact b{color:#fff}
.contact .mail{color:var(--footer-head)}
.social-label{font-size:11px;margin:20px 0 10px}
.social{display:flex}
.social i{width:40px;height:34px;border:1px solid #555;display:flex;align-items:center;justify-content:center}
.social i::after{content:"";width:10px;height:10px;border-radius:50%;background:#ccc}
.hours li{list-style:none;font-size:11px;margin-bottom:6px}
.hours b{color:#fff;display:inline-block;width:64px}
.bottom-bar{height:43px;background:#0b0b0b;color:#777;font-size:11px;display:flex;justify-content:space-between;align-items:center;padding:0 185px}
</style>
</head>
<body>

<div class="topbar">
  <span><svg viewBox="0 0 16 16"><path d="M3 1l3 3-2 2c1 2 3 4 5 5l2-2 3 3-2 3C7 15 1 9 1 3z"/></svg>Call : +61 2 5550 1842</span>
  <span><svg viewBox="0 0 16 16"><path d="M6 2h8v12H6v-2h6V4H6zM1 7h7V4l4 4-4 4V9H1z"/></svg>Sign in (or) Logout</span>
  <span><svg viewBox="0 0 16 16"><path d="M1 2h3l2 8h8l2-6H5" stroke="#ccc" fill="none" stroke-width="1.6"/><circle cx="7" cy="13" r="1.5"/><circle cx="13" cy="13" r="1.5"/></svg>(0) items in cart | ($0.00)</span>
</div>

<header class="site-header">
  <a class="brand" href="#"><span class="brand-dot"></span><span>Tarrowby Oakleaf Club</span></a>
  <nav class="main-nav">
    <a class="active" href="#"><svg viewBox="0 0 16 16"><path d="M8 1l7 7h-2v7H9v-4H7v4H3V8H1z"/></svg>Home</a>
    <a href="#"><svg viewBox="0 0 16 16"><path d="M2 2h12v12H2zM4 5h8v1H4zm0 3h8v1H4zm0 3h8v1H4z"/></svg>Menu</a>
    <a href="#"><svg viewBox="0 0 16 16"><path d="M1 3h14v10H1zm2 8h10l-3-4-2 3-2-2z"/></svg>Gallery</a>
    <a href="#"><svg viewBox="0 0 16 16"><path d="M1 2h3l2 8h8l2-6H5" stroke="currentColor" fill="none" stroke-width="1.6"/><circle cx="7" cy="13" r="1.5"/><circle cx="13" cy="13" r="1.5"/></svg>Shop</a>
    <a href="#"><svg viewBox="0 0 16 16"><path d="M11 1l4 4-9 9H2v-4z"/></svg>Blog</a>
    <a href="#"><svg viewBox="0 0 16 16"><path d="M1 3h14v12H1zm2 4v6h10V7zM4 1h2v3H4zm6 0h2v3h-2z"/></svg>Events</a>
    <a href="#"><svg viewBox="0 0 16 16"><path d="M1 3h14v10H1zm1 1l6 5 6-5"/></svg>Contact</a>
  </nav>
</header>

<section class="hero" role="img" aria-label="Restaurant wall with a hand drawn golden dragon mural on deep red, menu boards behind">
  <span class="hero-arrow prev"><svg viewBox="0 0 14 14"><path d="M10 1L4 7l6 6"/></svg></span>
  <span class="hero-arrow next"><svg viewBox="0 0 14 14"><path d="M4 1l6 6-6 6"/></svg></span>
  <div class="hero-dots"><i></i><i></i><i></i><i></i><i></i></div>
</section>

<main class="container">
  <section class="features">
    <article class="feature">
      <svg viewBox="0 0 66 66"><circle cx="33" cy="33" r="20" fill="#f6b21b"/><circle cx="33" cy="33" r="12" fill="#f9cd58"/><path d="M6 12v16M3 12v8a3 3 0 006 0v-8M6 28v26" stroke="#f6b21b" stroke-width="3" fill="none"/><path d="M60 12c-5 2-5 14 0 16v26" stroke="#f6b21b" stroke-width="3" fill="none"/></svg>
      <h3>Banquets</h3>
      <p>Sed ut perspiciatis unde omnis iste natus error sit voluptatem accusantium doloremque laudantium, totam rem aperiam.</p>
    </article>
    <article class="feature">
      <svg viewBox="0 0 66 66"><circle cx="40" cy="16" r="9" fill="#2f9a4a"/><path d="M34 22L18 52" stroke="#2f9a4a" stroke-width="5" stroke-linecap="round"/><path d="M18 52c-4 6-10 6-10 10" stroke="#2f9a4a" stroke-width="2" fill="none"/></svg>
      <h3>Shows</h3>
      <p>Sed ut perspiciatis unde omnis iste natus error sit voluptatem accusantium doloremque laudantium, totam rem aperiam.</p>
    </article>
    <article class="feature">
      <svg viewBox="0 0 66 66"><circle cx="33" cy="33" r="22" fill="#e8521e"/><path d="M11 33h44M33 11v44M17 17c8 8 8 24 0 32M49 17c-8 8-8 24 0 32" stroke="#8a2a0a" stroke-width="2" fill="none"/></svg>
      <h3>Games</h3>
      <p>Sed ut perspiciatis unde omnis iste natus error sit voluptatem accusantium doloremque laudantium, totam rem aperiam.</p>
    </article>
    <article class="feature">
      <svg viewBox="0 0 66 66"><path d="M4 20l24 9v8L4 46zM62 20l-24 9v8l24 9z" fill="#3a56a8"/><rect x="27" y="26" width="12" height="14" rx="3" fill="#2a4088"/></svg>
      <h3>Parties</h3>
      <p>Sed ut perspiciatis unde omnis iste natus error sit voluptatem accusantium doloremque laudantium, totam rem aperiam.</p>
    </article>
  </section>

  <h2 class="section-title order-title">Order Online</h2>
  <section class="products">
    <article class="product">
      <div class="photo p1" role="img" aria-label="Grilled chicken fillet with salsa and sour cream"></div>
      <div class="name">Grilled Chicken Fillet Salsa <span class="veg"></span></div>
      <div class="buy"><a class="btn" href="#">Add To Cart</a><span class="price">$18.50</span></div>
    </article>
    <article class="product">
      <div class="photo p2" role="img" aria-label="Grilled lamb cutlets on beetroot"></div>
      <div class="name">Grilled Lamb Cutlet <span class="veg"></span></div>
      <div class="buy"><a class="btn" href="#">Add To Cart</a><span class="price">$18.50</span></div>
    </article>
    <article class="product">
      <div class="photo p3" role="img" aria-label="Honey and lemon glazed chicken wings"></div>
      <div class="name">Honey and Lemon Chicken <span class="veg"></span></div>
      <div class="buy"><a class="btn" href="#">Add To Cart</a><span class="price">$16.50</span></div>
    </article>
  </section>

  <h2 class="section-title events-title">Recent Events</h2>
  <section class="events">
    <article class="event">
      <div class="event-side">
        <div class="event-date"><b>15</b><small>Feb<br>2014</small></div>
        <div class="event-stat">0 <svg viewBox="0 0 16 16"><path d="M1 2h14v9H6l-4 3v-3H1z"/></svg></div>
        <div class="event-stat icon"><svg viewBox="0 0 16 16"><path d="M1 3h14v10H1zm2 8h10l-3-4-2 3-2-2z"/></svg></div>
      </div>
      <div class="event-card">
        <div class="photo e1" role="img" aria-label="Club members gathered at the bar"></div>
        <h4>Dapibus Inibh bnec</h4>
        <p>Dasum modo typi, qui nibh euismod tincidunt ullao reet, quis nostrud exerci tation ullam corper suscipit lobortis nisl ut aliquip sen.</p>
        <div class="event-meta"><span>&#9632; Admin</span><span>&#9632; Branding</span></div>
      </div>
    </article>
    <article class="event">
      <div class="event-side">
        <div class="event-date"><b>06</b><small>Mar<br>2014</small></div>
        <div class="event-stat">0 <svg viewBox="0 0 16 16"><path d="M1 2h14v9H6l-4 3v-3H1z"/></svg></div>
        <div class="event-stat icon"><svg viewBox="0 0 16 16"><path d="M1 3h14v10H1zm2 8h10l-3-4-2 3-2-2z"/></svg></div>
      </div>
      <div class="event-card">
        <div class="photo e2" role="img" aria-label="Red restaurant menu board"></div>
        <h4>Nam laoreet adcing</h4>
        <p>Typi non habent claritatem insitam; est usus legentis in iis qui facit eorum claritatem. Inve ligationes demonstraverunt lectores lege.</p>
        <div class="event-meta"><span>&#9632; Admin</span><span>&#9632; Branding</span><span>&#9632; Food</span></div>
      </div>
    </article>
  </section>
  <div class="pager">Page 1 of 2 <a class="current" href="#">1</a><a href="#">2</a></div>

  <h2 class="section-title spec-title">Our Specialities</h2>
  <nav class="tabs"><a class="active" href="#">Club Meeting</a><a href="#">Wedding Orders</a><a href="#">Birthday Specials</a><a href="#">Parties</a></nav>
  <div class="tab-panel">
    <h3>All you need is to fill out this form</h3>
    <p>Investigationes demonstraverunt lectores legere me lius quod ii legunt saepius. Claritas est etiam processus dynus, qui sequitur mutationem consuetudium lectorum. Mirum est notare quam littera gothica, quam nunc putamus parum claram, anteposuerit litterarum formas humanitatis per seacula quarta decima et quinta decima. Eodem modo typi, qui nunc nobis videntur parum clari, fiant sollemnes in futurum. mutationem consuetudium lectorum. Mirum est notare quam littera gothica.</p>
  </div>

  <h2 class="section-title upcoming-title">Upcoming Events</h2>
  <section class="upcoming">
    <article>
      <div class="photo u1" role="img" aria-label="Friends enjoying drinks at the bar"></div>
      <h4>Live Band: Copper Lanterns</h4>
      <div class="when"><svg viewBox="0 0 16 16"><path d="M1 3h14v12H1zm2 4v6h10V7z"/></svg>Apr 21,2014 09:00 pm</div>
      <p>Dolor sit amet, consectetuer adipiscing elit, sed diam nonummy euismod tincidunt ut...</p>
    </article>
    <article>
      <div class="photo u2" role="img" aria-label="Guests raising glasses at a wine tasting"></div>
      <h4>Annual Wine Tasting</h4>
      <div class="when"><svg viewBox="0 0 16 16"><path d="M1 3h14v12H1zm2 4v6h10V7z"/></svg>May 07,2014 07:00 pm</div>
      <p>Aliquam erat volutpat. Ut wisi enim ad minim veniam, quis nostrud exerci tation ullamt...</p>
    </article>
    <article>
      <div class="photo u3" role="img" aria-label="Reader with a book in a quiet lounge"></div>
      <h4>Book Readers Club</h4>
      <div class="when"><svg viewBox="0 0 16 16"><path d="M1 3h14v12H1zm2 4v6h10V7z"/></svg>May 18,2014 10:00 am</div>
      <p>Curabitur adipiscing tellus ac molestie suscipit, vivamus fringilla felis, tempor malesuada odio nulla...</p>
    </article>
  </section>

  <section class="newsletter">
    <h3>Sign Up to our Newsletter</h3>
    <p>You'll be the first to hear about news, events, specials, limited-time offers, and more.</p>
    <form><input type="text" value="Your Name" aria-label="Your Name"><input type="text" value="Your Email" aria-label="Your Email"><button type="button">Submit</button></form>
  </section>
</main>

<footer class="site-footer">
  <div class="footer-cols">
    <div>
      <h5>Recent Posts</h5>
      <div class="post"><span class="thumb" role="img" aria-label="Post thumbnail"></span><div><b>Dapibus Inibh bnec</b>Eodem modo typi, qui nunc nobis videntur futurum.</div></div>
      <div class="post"><span class="thumb" role="img" aria-label="Post thumbnail"></span><div><b>Nam laoreet adcing</b>Duis autem vel eum iriure dolor in hendrerit in velit.</div></div>
      <div class="post"><span class="thumb" role="img" aria-label="Post thumbnail"></span><div><b>Phasellus molestie</b>Nam liber tempor cum soluta nobis eleifend option congue.</div></div>
    </div>
    <div>
      <h5>Photo Stream</h5>
      <div class="gallery" role="img" aria-label="Grid of club and restaurant photos"><i></i><i></i><i></i><i></i><i></i><i></i><i></i><i></i><i></i></div>
    </div>
    <div class="contact">
      <h5>Contact Us</h5>
      <ul>
        <li><svg viewBox="0 0 16 16"><path d="M8 0a5 5 0 015 5c0 4-5 11-5 11S3 9 3 5a5 5 0 015-5zm0 3a2 2 0 100 4 2 2 0 000-4z"/></svg><span><b>Address:</b> 42 Harbour Lane, Tarrowby, New South Wales 2399</span></li>
        <li><svg viewBox="0 0 16 16"><path d="M3 1l3 3-2 2c1 2 3 4 5 5l2-2 3 3-2 3C7 15 1 9 1 3z"/></svg><span><b>Phone:</b> +61 2 5550 1842</span></li>
        <li><svg viewBox="0 0 16 16"><path d="M1 3h14v10H1zm1 1l6 5 6-5"/></svg><span><b>Mail:</b> <span class="mail">info@tarrowbyclub.com</span></span></li>
      </ul>
      <p class="social-label">We are Social:</p>
      <div class="social"><i></i><i></i><i></i><i></i></div>
    </div>
    <div class="hours">
      <h5>Hours</h5>
      <ul>
        <li><b>Mon:</b>9:30 am - 7:00 pm</li>
        <li><b>Tue:</b>9:30 am - 7:00 pm</li>
        <li><b>Wed - Thu:</b>9:30 am - 8:30 pm</li>
        <li><b>Fri:</b>9:30 am - 10:30 pm</li>
        <li><b>Sat:</b>9:30 am - 9:00 pm</li>
        <li><b>Sun:</b>11:00 am - 8:00 pm</li>
      </ul>
    </div>
  </div>
</footer>
<div class="bottom-bar"><span>&copy; Copyright : Tarrowby Oakleaf Club 2014</span><span>Home | About | Menu | Shop | Blog | Contact Us</span></div>

</body>
</html>
```